Business Card for Freelance Copywriting & Web Design Business

Hi! I have a logo but want a new business card. Here's a better idea of what I'm thinking:
-Brand new double-sided business card, rounded cards, embossed logo, nice quality paper
-Include phone (604-382-9145), email (hello@linnearowatt.org), and website (www.linnearowatt.org). No address, please, since I service clients worldwide.
-I'd like the fonts to match those on my website (www.linnearowatt.org). I had to purchase the one font (Born Ready), attached. I'm not sure which version was used on my site so I included all that I purchased. The secondary font is Helvetica
-I'd also like the tagline "Powerful Words. Impressive Results." included.
-My primary brand colour is the teal, colour #19ADC3
Linnea Rowatt | Linnea Rowatt Copywriting & Web Design <hello@linnearowatt.org>
-I'd also like the following services listed on the new cards:
SEO Website Content
SEO Blog Content
SEO Website Design
Contact Information for Business Card
as stated in brief
Font styles to use
Other font styles liked:
- See brief
Look and feel
Each slider illustrates characteristics of the customer's brand and the style your logo design should communicate.

```html
<!DOCTYPE html>
<html lang="en">
<head>
<meta charset="utf-8">
<title>Linnea Rowatt Copywriting &amp; Web Design – Business Card</title>
<link href="https://fonts.googleapis.com/css2?family=Lato:wght@300;400;700&family=Roboto:wght@400&display=swap" rel="stylesheet">
<style>
  :root {
    --teal: #19adc3;
    --ink: #1a1a1a;
    --paper: #ffffff;
    --backdrop: #929292;
    --swoosh-grey: #e4e2e2;
    --divider: #9a9a9a;
  }
  * { box-sizing: border-box; margin: 0; padding: 0; }
  html, body { width: 1200px; height: 900px; overflow: hidden; }
  body { background: var(--backdrop); position: relative; font-family: "Lato", sans-serif; }

  .card { position: absolute; width: 539px; height: 308px; overflow: hidden; }

  /* Front */
  .card--front {
    left: 324px; top: 122px;
    background: var(--teal);
    border: 3px solid var(--paper);
    border-radius: 32px 0 32px 0;
  }
  .front-logo {
    position: absolute; left: 0; right: 0; top: 128px;
    text-align: center;
    font-family: "Lato", sans-serif; font-weight: 700;
    font-size: 42px; color: var(--ink); letter-spacing: 0.5px;
  }

  /* Back */
  .card--back {
    left: 324px; top: 450px;
    background: var(--paper);
    border-radius: 0 32px 0 32px;
  }
  .back-decoration {
    position: absolute; left: 75px; top: 0; width: 430px; height: 80px;
    background: radial-gradient(ellipse at 50% 20%, rgba(25,173,195,0.12), rgba(25,173,195,0) 70%);
  }
  .back-logo {
    position: absolute; left: 20px; width: 210px; top: 120px;
    text-align: center;
    font-family: "Lato", sans-serif; font-weight: 700;
    font-size: 24px; color: var(--ink);
  }
  .divider { position: absolute; left: 244px; top: 78px; width: 1px; height: 112px; background: var(--divider); }

  .contact-block { position: absolute; left: 275px; top: 76px; }
  .person-name { font-weight: 700; font-size: 26px; color: var(--teal); line-height: 1.1; letter-spacing: 0.2px; }
  .person-title { font-weight: 400; font-size: 14.5px; color: var(--ink); margin-top: 1px; }
  .contact-list { list-style: none; margin-top: 14px; }
  .contact-list li {
    display: flex; align-items: center; gap: 8px;
    font-weight: 300; font-size: 14px; color: var(--ink); height: 18.5px;
  }
  .contact-list svg { width: 8px; height: 8px; fill: var(--teal); flex: none; }

  .services {
    position: absolute; left: 0; right: 0; top: 220px; text-align: center;
    font-family: "Roboto", sans-serif; font-size: 14.5px; color: var(--ink);
  }
  .services .sep { color: var(--teal); margin: 0 3px; }

  .swoosh { position: absolute; left: 0; bottom: 0; width: 539px; height: 60px; }
  .tagline {
    position: absolute; right: 18px; bottom: 10px;
    font-family: "Roboto", sans-serif; font-size: 14.5px; color: var(--paper);
  }
</style>
</head>
<body>

  <section class="card card--front" aria-label="Business card front">
    <div class="front-logo">Linnea Rowatt</div>
  </section>

  <section class="card card--back" aria-label="Business card back">
    <div class="back-decoration" role="img" aria-label="Faint decorative brand flourish"></div>

    <div class="back-logo">Linnea Rowatt</div>
    <div class="divider"></div>

    <div class="contact-block">
      <h1 class="person-name">LINNEA ROWATT</h1>
      <p class="person-title">Owner and Freelance Copywriter</p>
      <ul class="contact-list">
        <li><svg viewBox="0 0 10 10" aria-hidden="true"><path d="M2 0.5 L3.8 2.6 L2.8 3.6 C3.4 5 4.9 6.5 6.4 7.2 L7.4 6.2 L9.5 8 L8.3 9.5 C4.5 9 1 5.5 0.5 1.7 Z"/></svg>604-382-9145</li>
        <li><svg viewBox="0 0 10 10" aria-hidden="true"><path d="M0 2 H10 V8 H0 Z M0.8 2.6 L5 5.6 L9.2 2.6" fill="var(--teal)"/><path d="M0.8 2.6 L5 5.6 L9.2 2.6" stroke="#fff" stroke-width="0.9" fill="none"/></svg>hello@linnearowatt.org</li>
        <li><svg viewBox="0 0 10 10" aria-hidden="true"><circle cx="5" cy="5" r="4.6"/></svg>www.linnearowatt.org</li>
      </ul>
    </div>

    <p class="services">SEO Website Content<span class="sep">|</span>SEO Blog Content<span class="sep">|</span>SEO Website Design</p>

    <svg class="swoosh" viewBox="0 0 539 60" aria-hidden="true">
      <path d="M15 60 C150 30 330 14 520 12 C360 22 220 38 130 60 Z" fill="var(--swoosh-grey)"/>
      <path d="M135 60 C230 38 380 24 539 22 L539 60 Z" fill="var(--teal)"/>
    </svg>
    <p class="tagline">Powerful Words. Impressive Results.</p>
  </section>

</body>
</html>
```